Blue Heron Courier & Delivery Services needs a flyer

We need an introductory flyer for a new company based in Yellowknife, Northwest Territories,Canada. Our company name is Blue Heron Courier & Delivery Services. We will be handling envelopes and small packages up to 20 pounds. We expect 20 percent of our business to come from residential customers and 80 percent from the business community including lawyers, doctors, engineers and government offices. The main message that we will try to convey in this flyer is that we are a new and exciting company that promises to make 100% customer satisfaction our number one goal. I would like the layout to be elegant and simple and certainly not cluttered. It will be a single sided flyer. Text should be easy to read and most likely at most two fonts. I would like one stunning image or photo relating to the courier business and message. There should be plenty of white space throughout the flyer and nice margins on all sides. I would like my flyer to be 8.5 inches by 11 inches and it should read from top to bottom. . I would like a nice big bold headline that in some way mentions " Special Offer- Up to 100% Off. You can change the wording if you have a better idea. Throughout the flyer you can highlight and italicize for emphasis. Please try to use bullet points for my five main reasons for hiring our company which are: you will be 100% satisfied with each delivery or you will be given a complete refund no questions asked, your envelope or package will be delivered on time every time, you will always be treated throughout the delivery process in a professional manner, you will be given the widest selection in Yellowknife of price points and delivery options , you can trust us with your most important and time sensitive deliveries. Try to incorporate something next to these five points to really draw attention like a check mark, star etc.... I would prefer if my company name and contact info is in the bottom third of the flyer. My email is blueheroncourieryk@mailbox-example.net. My phone number is 867-312-7794. It might be a good idea to have my phone number also at the top of the flyer someplace after the headline saying like Call Now!!! you can use boxes, borders and contrasting bold colors to bring flyer to life. I have a testimonial from a business owner that I dealt with when I ran another business which would be nice to have included . " While receiving daily deliveries for 18 years from Calvin Marsh I found him to be punctual , reliable and efficient " Glen Potter, owner of Potter and Lindqvist Trading LTD, Yellowknife,NWT. I thought perhaps at the top of flyer after the headline perhaps in some way you could say Yellowknife's newest and best courier and delivery service is pleased to offer the following stunning discounts: then you could list the three special offers: 1) First 5 businesses to book regular scheduled deliveries will get 100% off their first delivery. 2) First 5 businesses to book a single delivery will get 50% off that delivery. 3) First 5 residential customers to book a delivery will receive 25% off that delivery. I thought you could mention my name somewhere. Calvin Marsh. Owner has lived in Yellowknife for 42 years and has 20 years experience doing performing important and time sensitive deliveries. Perhaps you could mention somewhere that we will have a couple of ongoing discounts also which will be 1) seniors discounts. 2) regular scheduled deliveries discounts. I have suggested colors but if you have other ideas I would certainly look at them. Our business tag line is. On Time Every Time
Target Market(s)
Business owners typically males 30-50 years old
Industry/Entity Type
Delivery Service
Requirements
Must have
- Done in CMYK mode sufficient bleed size for printing
Nice to have
- Nothing set in stone. I recently had my logo design uploaded to this brief. It is up to you if you feel it should be included in the flyer.
Should not have
- I am willing to look at any design

```html
<!DOCTYPE html>
<html lang="en">
<head>
<meta charset="utf-8">
<title>Blue Heron Courier Service – Special Offer Flyer</title>
<link rel="stylesheet" href="https://fonts.googleapis.com/css2?family=Arimo:wght@400;700&family=Roboto+Condensed:wght@400;700&family=Tinos:ital,wght@1,700&family=Caveat:wght@500&display=swap">
<style>
:root{
  --page-bg:#e9e9e9;
  --paper:#f4f3f1;
  --paper-light:#ffffff;
  --red:#b8191b;
  --gold:#f6c75a;
  --ink:#1d1d1d;
  --ink-soft:#333333;
  --muted:#555555;
  --road:#4b4b4b;
  --yellow:#ffe000;
  --star:#f7c51c;
  --white:#ffffff;
}
*{margin:0;padding:0;box-sizing:border-box}
html,body{width:1200px;height:1000px;overflow:hidden}
body{background:var(--page-bg);font-family:"Arimo",Arial,sans-serif;color:var(--ink);position:relative}

.flyer{position:absolute;left:182px;top:168px;width:823px;height:640px;overflow:hidden;
  background:radial-gradient(ellipse at 70% 40%,var(--paper-light) 0%,var(--paper) 60%,#e6e4e1 100%);
  box-shadow:0 6px 14px rgba(0,0,0,.28)}
.abs{position:absolute}

.offer-corner{left:0;top:0;width:340px;height:285px}
.offer-line{position:absolute;width:340px;text-align:center;white-space:nowrap;
  transform:translate(-50%,-50%) rotate(-40deg);transform-origin:50% 50%;
  font-family:"Arimo",Arial,sans-serif;font-weight:700;line-height:1}
.offer-upto{left:78px;top:44px;font-size:33px;color:var(--gold)}
.offer-pct{left:104px;top:76px;font-size:33px;color:var(--gold)}
.offer-special{left:140px;top:118px;font-size:44px;color:var(--white)}

.courier-photo{left:168px;top:36px;width:260px;height:380px;border-radius:120px 120px 30px 30px;
  background:radial-gradient(ellipse at 50% 30%,#e8d3b2 0%,#d8bf98 45%,rgba(216,191,152,0) 75%)}

.brand{right:20px;top:24px;text-align:right}
.brand-name{font-family:"Arimo",Arial,sans-serif;font-weight:700;font-size:30px;color:var(--ink);letter-spacing:.5px;display:flex;align-items:center;gap:10px;justify-content:flex-end}
.brand-name .mark{width:14px;height:14px;background:var(--ink);display:inline-block}
.contact{right:22px;top:106px;text-align:right;font-family:"Roboto Condensed",Arial,sans-serif;font-size:15.5px;color:var(--ink-soft);line-height:23px}
.contact .small{font-size:13.5px}

.reasons{left:308px;top:198px;width:500px;list-style:none;font-family:"Roboto Condensed",Arial,sans-serif;font-size:14.6px;color:var(--ink-soft);line-height:16px}
.reasons li{position:relative;padding-left:32px;margin-bottom:12px}
.reasons li svg{position:absolute;left:0;top:-2px;width:22px;height:22px}

.call-now{right:16px;top:384px;font-family:"Tinos",serif;font-style:italic;font-weight:700;font-size:56px;letter-spacing:1px;color:var(--ink);line-height:1}
.call-phone{right:34px;top:446px;font-family:"Roboto Condensed",Arial,sans-serif;font-size:18px;color:var(--ink-soft);display:flex;align-items:center;gap:4px}
.call-phone svg{width:18px;height:18px}

.testimonial{left:14px;top:302px;width:190px;font-family:"Roboto Condensed",Arial,sans-serif;font-size:12.8px;line-height:19px;color:var(--muted)}
.testimonial cite{display:block;margin-top:6px;font-style:italic;font-weight:700;font-size:13px;line-height:14px;color:var(--ink-soft)}
.testimonial .role{display:block;font-style:normal;font-weight:400;font-size:9px;line-height:10px}

.road{left:0;top:0;width:823px;height:640px}

.discounts{left:12px;top:450px;width:530px;font-family:"Arimo",Arial,sans-serif;font-weight:700;color:var(--white)}
.discounts h2{font-size:19px;line-height:24px;font-weight:700}
.discounts h2 .hl{color:var(--yellow)}
.discounts h2 .l1{display:block;padding-left:70px}
.discounts ol{list-style:none;margin-top:6px;font-family:"Roboto Condensed",Arial,sans-serif;font-size:13.8px;line-height:15px;color:#f0f0f0}
.discounts ol li{padding-left:22px;text-indent:-16px;margin-bottom:5px;margin-left:6px}

.owner-icon{left:574px;top:502px;width:44px;height:44px}
.owner-name{left:634px;top:504px;font-family:"Caveat",cursive;font-size:34px;color:var(--white);line-height:1}
.owner-box{left:520px;top:552px;width:303px;height:88px}
.owner-bio{right:14px;top:560px;width:250px;text-align:right;font-family:"Roboto Condensed",Arial,sans-serif;font-size:12.6px;line-height:13.5px;color:var(--ink)}
.owner-web{right:14px;top:608px;font-family:"Arimo",Arial,sans-serif;font-weight:700;font-size:13.6px;color:var(--ink)}
</style>
</head>
<body>
<main class="flyer">

  <div class="abs courier-photo" role="img" aria-label="Photo of a smiling courier in a beige uniform running with a clipboard and a cardboard parcel"></div>

  <svg class="abs offer-corner" viewBox="0 0 340 285" aria-hidden="true">
    <polygon points="0,0 338,0 0,283" fill="var(--red)"/>
    <line x1="14" y1="176" x2="222" y2="2" stroke="#ffffff" stroke-opacity=".6" stroke-width="1"/>
  </svg>
  <div class="offer-line offer-upto">Up To</div>
  <div class="offer-line offer-pct">100% Off</div>
  <div class="offer-line offer-special">Special Offer</div>

  <div class="abs brand">
    <div class="brand-name"><span class="mark"></span>Blue Heron Courier Service, Inc.</div>
  </div>
  <div class="abs contact">
    118 Franklin Ave., Yellowknife, NT X1A 2L9<br>
    Phone: (867) 312-7794 &nbsp;|&nbsp; Fax: 867-312-7795<br>
    <span class="small">Email: specials@blueheroncourier-example.net</span>
  </div>

  <ul class="abs reasons">
    <li><svg viewBox="0 0 24 24"><polygon points="12,1 15,9 23,9 16.5,14 19,22 12,17 5,22 7.5,14 1,9 9,9" fill="var(--star)"/></svg>You will be 100% satisfied with each delivery or you will be given a complete refund no questions asked.</li>
    <li><svg viewBox="0 0 24 24"><polygon points="12,1 15,9 23,9 16.5,14 19,22 12,17 5,22 7.5,14 1,9 9,9" fill="var(--star)"/></svg>Your envelope or package will be delivered on time every time.</li>
    <li><svg viewBox="0 0 24 24"><polygon points="12,1 15,9 23,9 16.5,14 19,22 12,17 5,22 7.5,14 1,9 9,9" fill="var(--star)"/></svg>You will always be treated throughout the delivery process in a professional manner.</li>
    <li><svg viewBox="0 0 24 24"><polygon points="12,1 15,9 23,9 16.5,14 19,22 12,17 5,22 7.5,14 1,9 9,9" fill="var(--star)"/></svg>You will be given the widest selection in Yellowknife of price points and delivery options.</li>
    <li><svg viewBox="0 0 24 24"><polygon points="12,1 15,9 23,9 16.5,14 19,22 12,17 5,22 7.5,14 1,9 9,9" fill="var(--star)"/></svg>You can trust us with your most important and time sensitive deliveries.</li>
  </ul>

  <blockquote class="abs testimonial">
    " While receiving daily deliveries for 18 years from Calvin Marsh I found him to be punctual , reliable and efficient "
    <cite>Glen Potter<span class="role">owner of Potter and Lindqvist Trading LTD, Yellowknife,NWT</span></cite>
  </blockquote>

  <svg class="abs road" viewBox="0 0 823 640" aria-hidden="true">
    <path d="M0,425 L330,425 C450,425 520,432 600,452 C680,472 760,482 823,474 L823,640 L0,640 Z" fill="var(--road)"/>
    <path d="M0,436 L330,436 C450,436 520,443 600,463 C680,483 760,493 823,485" fill="none" stroke="#ffffff" stroke-width="2.5" stroke-dasharray="8 14"/>
    <path d="M0,420 L330,420 C450,420 520,427 600,447 C680,467 760,477 823,469" fill="none" stroke="#9a9a9a" stroke-width="2"/>
  </svg>

  <div class="abs call-now">CALL NOW</div>
  <div class="abs call-phone">
    <svg viewBox="0 0 24 24"><polygon points="12,1 15,9 23,9 16.5,14 19,22 12,17 5,22 7.5,14 1,9 9,9" fill="var(--star)"/></svg>
    (867) 312-7794
    <svg viewBox="0 0 24 24"><polygon points="12,1 15,9 23,9 16.5,14 19,22 12,17 5,22 7.5,14 1,9 9,9" fill="var(--star)"/></svg>
  </div>

  <section class="abs discounts">
    <h2><span class="hl l1">Yellowknife's newest and</span>BEST COURIER AND DELIVERY SERVICE<br><span class="hl">is pleased to offer the following stunning discounts:</span></h2>
    <ol>
      <li>1) First 5 businesses to book regular scheduled deliveries will get 100% off their first delivery.</li>
      <li>2) First 5 businesses to book a single delivery will get 50% off that delivery.</li>
      <li>3) First 5 residential customers to book a delivery will receive 25% off that delivery.</li>
    </ol>
  </section>

  <svg class="abs owner-icon" viewBox="0 0 44 44" aria-hidden="true">
    <circle cx="22" cy="13" r="9" fill="var(--yellow)"/>
    <path d="M4,42 C4,30 12,24 22,24 C32,24 40,30 40,42 Z" fill="var(--yellow)"/>
  </svg>
  <div class="abs owner-name">Calvin Marsh</div>

  <svg class="abs owner-box" viewBox="0 0 303 88" aria-hidden="true">
    <polygon points="38,0 303,0 303,88 0,88" fill="var(--yellow)"/>
  </svg>
  <p class="abs owner-bio">Owner has lived in Yellowknife for 42 years and has 20 years experience doing performing important and time sensitive deliveries.</p>
  <div class="abs owner-web">www.blueheroncourier-example.net</div>

</main>
</body>
</html>
```